Consulting/Brand Licensing business needs business card

We need a business card created for our IP company, that also does consulting and brand licensing. We would like this card to be vague, as our other business' are in the cannabis industry and this is a non-cannabis touching entity. Perhaps something that hints vaguely at the industry without alerting or possibly offending the receiver.

Target Market(s)

CEOs/Key Decision Makers/Industry Leaders

Contact Information for Business Card

No address, simply list Seattle, WA. Phone: 206-555-0143. Name: Dario Lindqvist // email: Dario@velmarcoast.com

Colors

Designer to choose colors to be used in the design.

Requirements
Must have
• Logo, Name, Email, Phone number, "Consulting, Licensing and Branding Specialists"
Nice to have
• We would like this to be more professional than playful.

```html
<!DOCTYPE html>
<html lang="en">
<head>
<meta charset="utf-8">
<title>Velmar Coast – Business Card</title>
<link href="https://fonts.googleapis.com/css2?family=Roboto:wght@400;500&family=Roboto+Condensed:wght@400;700&family=Questrial&display=swap" rel="stylesheet">
<style>
  :root {
    --page-bg: #e9e6e2;
    --brand-orange: #e04c2c;
    --card-white: #ffffff;
    --card-back: #f1f1f1;
    --ink-dark: #222222;
    --ink-muted: #444444;
    --on-orange: #ffffff;
    --divider: rgba(255,255,255,0.55);
  }
  * { margin: 0; padding: 0; box-sizing: border-box; }
  html, body { width: 1200px; height: 960px; overflow: hidden; }
  body { background: var(--page-bg); position: relative; font-family: "Roboto", sans-serif; }

  .card { position: absolute; width: 600px; height: 343px; box-shadow: 0 3px 8px rgba(0,0,0,0.18); }

  /* Front */
  .card-front { left: 314px; top: 129px; background: var(--card-white); }
  .front-band { position: absolute; left: 0; top: 72px; width: 100%; height: 198px; background: var(--brand-orange); }
  .front-wordmark {
    position: absolute; left: 40px; top: 0; width: 262px; height: 198px;
    display: flex; align-items: center; justify-content: center;
    font-family: "Roboto Condensed", sans-serif; font-weight: 700; font-size: 38px;
    line-height: 1; color: var(--on-orange); letter-spacing: 1px; text-transform: uppercase;
  }
  .front-divider { position: absolute; left: 306px; top: 27px; width: 1px; height: 145px; background: var(--divider); }
  .contact-block { position: absolute; left: 338px; top: 34px; color: var(--on-orange); }
  .person-name { font-family: "Roboto Condensed", sans-serif; font-weight: 700; font-size: 21px; line-height: 24px; text-transform: uppercase; }
  .person-title { font-family: "Roboto Condensed", sans-serif; font-size: 15px; line-height: 18px; margin-left: -1px; }
  .person-city { font-size: 14px; line-height: 18px; margin-top: 6px; }
  .contact-list { list-style: none; margin-top: 7px; }
  .contact-list li { display: flex; align-items: center; font-size: 14px; line-height: 19.5px; }
  .contact-list svg { width: 13px; height: 13px; margin-right: 8px; fill: var(--on-orange); flex: none; }

  /* Back */
  .card-back { left: 311px; top: 488px; background: var(--card-back); text-align: center; }
  .back-wordmark {
    position: absolute; left: 0; top: 96px; width: 100%;
    font-family: "Roboto Condensed", sans-serif; font-weight: 700; font-size: 56px;
    line-height: 1; color: var(--brand-orange); letter-spacing: 1px; text-transform: uppercase;
  }
  .company-name { position: absolute; left: 0; top: 208px; width: 100%; font-family: "Questrial", sans-serif; font-size: 25px; color: var(--ink-dark); }
  .tagline { position: absolute; left: 0; top: 287px; width: 100%; font-size: 14.5px; color: var(--ink-muted); letter-spacing: 0.2px; }
</style>
</head>
<body>
  <section class="card card-front">
    <div class="front-band">
      <div class="front-wordmark">Velmar Coast</div>
      <div class="front-divider"></div>
      <div class="contact-block">
        <p class="person-name">Dario Lindqvist</p>
        <p class="person-title">COO/FOUNDER</p>
        <p class="person-city">Seattle, WA.</p>
        <ul class="contact-list">
          <li><svg viewBox="0 0 24 24" aria-hidden="true"><path d="M6.6 10.8a15.1 15.1 0 0 0 6.6 6.6l2.2-2.2c.3-.3.7-.4 1-.2 1.1.4 2.3.6 3.6.6.6 0 1 .4 1 1V20c0 .6-.4 1-1 1A17 17 0 0 1 3 4c0-.6.4-1 1-1h3.5c.6 0 1 .4 1 1 0 1.3.2 2.5.6 3.6.1.3 0 .7-.2 1z"/></svg>206-555-0143</li>
          <li><svg viewBox="0 0 24 24" aria-hidden="true"><path d="M2 5h20v14H2z M2 5l10 8 10-8" fill="none" stroke="#fff" stroke-width="0"/><path d="M2 5h20l-10 7.5zM2 7l10 7.5L22 7v12H2z"/></svg>Dario@velmarcoast.com</li>
          <li><svg viewBox="0 0 24 24" aria-hidden="true"><circle cx="12" cy="12" r="10"/><path d="M7 6c2 1 3 3 2 5s1 3 2 4-1 4-1 5M15 4c-1 2 1 3 3 3s2 3 1 5" stroke="#e04c2c" stroke-width="1.8" fill="none"/></svg>www.velmarcoast.com</li>
        </ul>
      </div>
    </div>
  </section>

  <section class="card card-back">
    <div class="back-wordmark">Velmar Coast</div>
    <p class="company-name">Velmar Coast, Inc</p>
    <p class="tagline">Consulting, Licensing and Branding Specialists</p>
  </section>
</body>
</html>
```